Speisekarten für griechisches Restaurant
Zielgruppe
modernes griechisches Restaurant
Aufgabenstellung
neues modernen helles design ,
nach Durchsicht aus meinen Vorlangen, sollten ein paar Anpassung am text und preisen noch durchgeführt werden.
aus der pdf datei,, ist ab Seite 7 die richtige Speisekarte,, vorher sind nur entwürfe vom mir, diese bitte ignorieren.

```html
<!DOCTYPE html>
<html lang="de">
<head>
<meta charset="utf-8">
<title>Tiganakia – Pfannengerichte</title>
<link href="https://fonts.googleapis.com/css2?family=Great+Vibes&family=Barlow+Condensed:wght@600&family=Roboto:ital,wght@0,400;0,700;1,400&display=swap" rel="stylesheet">
<style>
  :root {
    --paper: #ffffff;
    --ink: #1d1d1b;
    --frame: #b9c79a;
    --accent: #8fa65a;
    --band: #e9ece3;
    --band-edge: #c8d0b6;
  }
  * { margin: 0; padding: 0; box-sizing: border-box; }
  html, body { width: 848px; height: 1200px; overflow: hidden; background: var(--paper); }
  .menu-page {
    position: relative; width: 848px; height: 1200px;
    background: var(--paper); color: var(--ink);
    font-family: "Roboto", Arial, sans-serif;
  }
  .deco { position: absolute; border-radius: 50%; }
  .deco--mushroom { left: -30px; top: 250px; width: 150px; height: 180px; background: radial-gradient(circle, #eceee9 0%, rgba(255,255,255,0) 70%); }
  .deco--garlic { right: -20px; top: 610px; width: 150px; height: 200px; background: radial-gradient(circle, #eceee9 0%, rgba(255,255,255,0) 70%); }
  .deco--veggies { left: -20px; top: 870px; width: 200px; height: 200px; background: radial-gradient(circle, #eeefeb 0%, rgba(255,255,255,0) 70%); }
  .deco--pan { right: -30px; top: 980px; width: 300px; height: 230px; background: radial-gradient(circle, #eceee9 0%, rgba(255,255,255,0) 70%); }

  .frame { position: absolute; left: 0; top: 0; }

  .title {
    position: absolute; left: 0; width: 848px; top: 32px; text-align: center;
    font-family: "Great Vibes", cursive; font-weight: 400;
    font-size: 168px; line-height: 1; letter-spacing: 2px; padding-left: 40px;
  }
  .subtitle {
    position: absolute; left: 472px; top: 190px;
    font-family: "Great Vibes", cursive; font-size: 48px; line-height: 1;
  }

  .column { position: absolute; text-align: center; width: 320px; }
  .column--left { left: 107px; }
  .column--right { left: 427px; }

  .dish { position: absolute; left: 0; width: 100%; }
  .dish__name {
    font-family: "Barlow Condensed", "Arial Narrow", sans-serif; font-weight: 600;
    font-size: 17px; letter-spacing: 0.3px; line-height: 20px; margin-bottom: 1px;
  }
  .dish__text { font-size: 11.5px; line-height: 16px; }
  .dish__text sup, .note sup { font-size: 6px; vertical-align: 5px; line-height: 0; }
  .dish__text em { font-style: italic; }
  .sauce { margin-top: 24px; }
  .note { position: absolute; left: 0; width: 100%; font-size: 11.5px; line-height: 18px; }
  .note strong { font-weight: 700; }

  .info-band {
    position: absolute; left: 97px; top: 932px; width: 690px; height: 70px;
    background: var(--band); border: 1px solid var(--band-edge);
    display: flex; align-items: center; justify-content: center; text-align: center;
    color: var(--accent); font-style: italic; font-size: 14px; line-height: 20px;
  }

  .brand {
    position: absolute; left: 0; width: 848px; top: 1082px;
    display: flex; align-items: center; justify-content: center; gap: 8px;
    font-family: "Roboto", Arial, sans-serif; font-size: 22px; color: var(--accent);
  }
  .brand__dot { width: 26px; height: 26px; border-radius: 50%; background: var(--accent); }

  .legal { position: absolute; left: 45px; top: 1140px; font-size: 8.5px; line-height: 12px; }
</style>
</head>
<body>
<div class="menu-page">
  <div class="deco deco--mushroom" role="img" aria-label="Zarte Linienzeichnung von Champignons"></div>
  <div class="deco deco--garlic" role="img" aria-label="Zarte Linienzeichnung einer Knoblauchknolle"></div>
  <div class="deco deco--veggies" role="img" aria-label="Zarte Linienzeichnung von Gemüse"></div>
  <div class="deco deco--pan" role="img" aria-label="Zarte Linienzeichnung einer Pfanne mit Gericht"></div>

  <svg class="frame" width="848" height="1200" viewBox="0 0 848 1200" aria-hidden="true">
    <g fill="none" stroke="var(--frame)" stroke-width="1.3">
      <polyline points="150,107 88,107 88,924"/>
      <polyline points="800,255 800,924"/>
      <path d="M97 924 h-12 v14 h12 M787 924 h12 v14 h-12"/>
    </g>
  </svg>

  <h1 class="title">Tiganakia</h1>
  <div class="subtitle">(Pfannengerichte)</div>

  <section class="column column--left">
    <div class="dish" style="top:398px">
      <h2 class="dish__name">43. ASTERI | 21,5</h2>
      <p class="dish__text">Schweinefilet-Medaillons mit<br>frischen Champignons und<br>Sauce nach Wahl</p>
      <p class="dish__text sauce">Asteri-/Pfeffer-Sauce <sup>6,A,C,F,G,I,J</sup><br>Pikante Sauce, verfeinert mit Weißwein <sup>6,A,C,F,G,I,J</sup></p>
    </div>
    <div class="dish" style="top:556px">
      <h2 class="dish__name">44. CHEF | 23,-</h2>
      <p class="dish__text">verschiedene Fleischsorten in einer<br>Tomaten-Knoblauch-Sauce<br>mit Creme-Fraiche<sup>F</sup> verfeinert</p>
    </div>
    <div class="dish" style="top:628px">
      <h2 class="dish__name">45. SKORDO | 23,-</h2>
      <p class="dish__text">verschiedene Fleischsorten<br>mit Knoblauch, Paprika, Zwiebeln und Fetakäse<sup>F</sup></p>
    </div>
    <p class="note" style="top:756px">Diese Gerichte werden von<br><strong>Salat und Patatakia</strong> begleitet</p>
  </section>

  <section class="column column--right">
    <div class="dish" style="top:398px">
      <h2 class="dish__name">46. GALOPOULA | 21,5</h2>
      <p class="dish__text">Putengeschnetzeltes mit frischen<br>Champignons, verfeinert mit einer<br>pikanten Sauce <sup>6,A,C,F,G,I,J</sup></p>
    </div>
    <div class="dish" style="top:500px">
      <h2 class="dish__name">47. MON AMOUR &nbsp;| 21,-</h2>
      <p class="dish__text">Hähnchenbrustfilet in einer<br><em>Spezial-Fetasauce</em><sup>F</sup></p>
    </div>
    <div class="dish" style="top:586px">
      <h2 class="dish__name">48. NAXOS | 24,-</h2>
      <p class="dish__text">Rumpsteak, Schweine- und Putenfilet<br>in einer <em>Spezial-Fetasauce</em><sup>F</sup><br>mit Zucchini und Auberginenwürfel</p>
    </div>
    <p class="note" style="top:700px">Diese Gerichte werden von<br><strong>Salat und Reis</strong> begleitet</p>
  </section>

  <div class="info-band">
    <p>Tiganaki ist ein traditionelles griechisches Gericht, das aus Fleisch,<br>Gemüse und einer Sauce besteht.</p>
  </div>

  <div class="brand"><span class="brand__dot"></span><span>Ilios Taverna</span></div>

  <p class="legal">Alle Preise in €. Änderungen mit Mehrwand<br>werden mit einem Aufpreis berechnet.</p>
</div>
</body>
</html>
```